Leading In-Home Tutoring Company Needs Web Banners

We need a suite of web banners for our re-marketing campaign. We are based in Melbourne and heading into the busiest time of the year with back to school and we would like to help guide parents to working with us via quality designed banners with the right CTAs. Banner specs as follows (W x H in pixels)
Medium Rectangle: 300 x 250
Vertical rectangle: 240 x 400
Banner: 468 x 60
Leaderboard: 728 x 90
Square: 250 x 250
Mobile leaderboard: 320 x 50
Updates

Hi designers I'm new to this and didn't realise that I had to upload all files at the beginning. I have images that can be used for this project. Just need to work out how to upload them. Added Sunday, January 22, 2017

Hi awesome designers... I've updated the brief now with new files :)

Target Market(s)

Mothers who value kids education. Our customer can be found having morning coffee with friends in her lycra as she prepares to go to the gym. Middle class, inner city and suburban Mums. Most likely on Chatterloom.

Industry/Entity Type

It Company

Font styles to use
Sans Serif

Colors
0692cd
fbed22
f47f39
ec1f27

Requirements
Must have
• Wording should include.
• What we do: 1:1, In-Home Tutoring
• Value proposition: The Best Tutor For Your Child
• Call to Action - Free Assessment > Find Out More
• Adjusted layout to suit the sizes. Use of image where possible to provide immediate graphic display of what we do
Nice to have
• Keep it simple, create an emotive connection. Kids matter to parents and they will pay for services if we can create banners that show we care and can help wtih their education.
Should not have
• Anything negative or use fear marketing

```html
<!DOCTYPE html>
<html lang="en">
<head>
<meta charset="utf-8">
<title>Learnwise – In-Home Tutoring Web Banners</title>
<link rel="stylesheet" href="https://fonts.googleapis.com/css2?family=Mulish:wght@400;600;700;800&family=Open+Sans:ital,wght@1,600&display=swap">
<style>
:root{
  --blue:#0a8fcc;
  --sky:#45b0ea;
  --orange:#f58a25;
  --yellow:#fbed22;
  --red:#bd2f3a;
  --ink:#2e6ea6;
  --white:#ffffff;
  --stage-hi:#ffffff;
  --stage-lo:#d9d9d9;
  --photo-a:#5b6f93;
  --photo-b:#a08a78;
  --photo-c:#e7e2dc;
}
*{box-sizing:border-box;margin:0;padding:0}
html,body{width:1200px;height:643px;overflow:hidden}
body{
  position:relative;
  font-family:"Mulish",Arial,sans-serif;
  background:radial-gradient(ellipse 55% 60% at 52% 50%,var(--stage-hi),var(--stage-lo));
}
.banner{
  position:absolute;overflow:hidden;background:var(--white);
  transform:scale(.8);transform-origin:0 0;
  box-shadow:0 3px 8px rgba(0,0,0,.35);
}
.banner > *{position:absolute}
.photo{background:linear-gradient(115deg,var(--photo-a) 0%,var(--photo-b) 45%,var(--photo-c) 75%,var(--photo-a) 100%)}
.brand{font-weight:700;color:var(--ink);white-space:nowrap;display:flex;align-items:center;gap:5px}
.brand i{display:inline-block;width:.55em;height:.55em;border-radius:50%;background:var(--orange)}
.cta{background:var(--red);color:var(--white);text-align:center;line-height:1.1;display:flex;flex-direction:column;align-items:center;justify-content:center}
.caret{width:12px;height:7px;margin-top:2px}
.w{color:var(--white)}
.y{color:var(--yellow)}
.o{color:var(--orange)}
.b{color:var(--blue)}
.s{color:var(--sky)}
strong{font-weight:800}
.center{text-align:center}

/* Medium rectangle 300x250 */
.medium{left:58px;top:106px;width:300px;height:250px}
.medium .headline{left:0;top:2px;width:128px;line-height:1.15}
.medium .ratio{font-size:38px;font-weight:800}
.medium .kind{font-size:24px}
.medium .kind2{font-size:25px;font-weight:800}
.medium .photo{left:128px;top:0;width:172px;height:190px}
.medium .value{left:0;top:104px;width:128px;height:86px;background:var(--orange);border-top:3px solid var(--yellow);font-size:16.5px;line-height:1.2;padding-top:4px}
.medium .notch{left:128px;top:122px;width:16px;height:34px}
.medium .brand{left:12px;top:214px;font-size:23px}
.medium .cta{left:140px;top:176px;width:160px;height:74px;border-radius:60px 0 0 70px/40px 0 0 74px;font-size:15px}

/* Square 250x250 */
.square{left:58px;top:350px;width:250px;height:250px}
.square .headline{left:0;top:6px;width:108px;line-height:1.15}
.square .ratio{font-size:34px;font-weight:800}
.square .kind{font-size:21px}
.square .kind2{font-size:21px;font-weight:800}
.square .photo{left:108px;top:0;width:142px;height:195px}
.square .value{left:0;top:96px;width:108px;height:99px;background:var(--orange);border-top:3px solid var(--yellow);font-size:19px;line-height:1.18;padding-top:6px}
.square .notch{left:108px;top:120px;width:14px;height:30px}
.square .brand{left:10px;top:226px;font-size:16px}
.square .cta{left:133px;top:186px;width:117px;height:58px;border-radius:50px 0 0 58px/30px 0 0 58px;font-size:12.5px}

/* Vertical rectangle 240x400 */
.vertical{left:354px;top:112px;width:240px;height:400px}
.vertical .brand{left:0;top:22px;width:240px;justify-content:center;font-size:22px}
.vertical .band{left:0;top:60px;width:240px;height:78px;background:var(--blue);line-height:1.05;padding-top:6px}
.vertical .ratio{font-size:38px;font-weight:800}
.vertical .kind{font-size:25px}
.vertical .rule{left:0;top:138px;width:240px;height:4px;background:var(--orange)}
.vertical .photo{left:0;top:142px;width:240px;height:138px}
.vertical .value{left:0;top:280px;width:240px;height:70px;font-size:20px;line-height:1.2;padding-top:5px}
.vertical .notch{left:105px;top:266px;width:30px;height:15px}
.vertical .base{left:0;top:346px;width:240px;height:54px;background:var(--sky)}
.vertical .cta{left:68px;top:338px;width:128px;height:58px;border-radius:0 0 64px 64px/0 0 44px 44px;font-size:13px}

/* Banner 468x60 */
.strip{left:583px;top:111px;width:468px;height:60px}
.strip .brand{left:10px;top:24px;font-size:14px}
.strip .band{left:108px;top:0;width:150px;height:60px;background:var(--blue);line-height:1.1;padding-top:5px}
.strip .notch{left:258px;top:12px;width:12px;height:36px}
.strip .photo{left:258px;top:0;width:114px;height:60px}
.strip .cta{left:372px;top:0;width:96px;height:60px;font-size:11px;font-weight:700}
.strip .cta .big{font-size:16px;font-weight:600}

/* Leaderboard 728x90 */
.leader{left:583px;top:207px;width:728px;height:90px}
.leader .brand{left:12px;top:34px;font-size:18px}
.leader .band{left:136px;top:0;width:248px;height:90px;background:var(--orange);line-height:1.05;padding-top:2px}
.leader .notch{left:382px;top:0;width:16px;height:90px}
.leader .photo{left:396px;top:0;width:190px;height:90px}
.leader .ratio{font-size:36px;font-weight:800}
.leader .kind{font-size:25px}
.leader .tag{font-family:"Open Sans",Arial,sans-serif;font-style:italic;font-weight:600;font-size:15px;margin-top:3px}
.leader .cta{left:586px;top:0;width:142px;height:90px;font-size:18px}
.leader .cta .big{font-size:26px}

/* Mobile leaderboard 320x50 */
.mobile{left:583px;top:330px;width:320px;height:50px}
.mobile .brand{left:6px;top:20px;font-size:13px}
.mobile .photo{left:124px;top:0;width:114px;height:50px}
.mobile .cta{left:238px;top:0;width:82px;height:50px;font-size:9.5px;font-weight:600}
.mobile .cta .big{font-size:14px}
</style>
</head>
<body>

<section class="banner medium" aria-label="Medium rectangle banner">
  <div class="photo" role="img" aria-label="Tutor helping a smiling schoolgirl with her books in front of a bookshelf"></div>
  <div class="headline center">
    <div class="ratio b">1<span class="o">:</span>1</div>
    <div class="kind s">In-Home</div>
    <div class="kind2 o">Tutoring</div>
  </div>
  <div class="value center w">The Best<br><strong>Tutor</strong><br>For Your<br><strong>Child</strong></div>
  <svg class="notch" viewBox="0 0 16 34"><polygon points="0,0 16,17 0,34" fill="var(--orange)"/></svg>
  <div class="brand">Learnwise<i></i></div>
  <div class="cta"><span>Click Here</span><span>Get a <strong>FREE</strong></span><span>Assessment</span>
    <svg class="caret" viewBox="0 0 12 7"><polyline points="1,6 6,1 11,6" fill="none" stroke="#fff" stroke-width="2"/></svg></div>
</section>

<section class="banner square" aria-label="Square banner">
  <div class="photo" role="img" aria-label="Tutor helping a smiling schoolgirl with her books in front of a bookshelf"></div>
  <div class="headline center">
    <div class="ratio b">1:1</div>
    <div class="kind o">In-Home</div>
    <div class="kind2 b">Tutoring</div>
  </div>
  <div class="value center w">The Best<br>Tutor<br>For Your<br>Child</div>
  <svg class="notch" viewBox="0 0 14 30"><polygon points="0,0 14,15 0,30" fill="var(--orange)"/></svg>
  <div class="brand">Learnwise<i></i></div>
  <div class="cta"><span>Click Here</span><span>Get a <strong>FREE</strong></span><span>Assessment</span>
    <svg class="caret" viewBox="0 0 12 7"><polyline points="1,6 6,1 11,6" fill="none" stroke="#fff" stroke-width="2"/></svg></div>
</section>

<section class="banner vertical" aria-label="Vertical rectangle banner">
  <div class="brand">Learnwise<i></i></div>
  <div class="band center">
    <div class="ratio y">1:1</div>
    <div class="kind w">In-Home <span class="y">Tutoring</span></div>
  </div>
  <div class="rule"></div>
  <div class="photo" role="img" aria-label="Tutor working through a book with a schoolboy at a desk"></div>
  <svg class="notch" viewBox="0 0 30 15"><polygon points="0,15 15,0 30,15" fill="#fff"/></svg>
  <div class="value center"><span class="s">The Best</span> <span class="o"><strong>Tutor</strong></span><br><span class="s">For Your</span> <span class="o"><strong>Child</strong></span></div>
  <div class="base"></div>
  <div class="cta"><span>Click Here</span><span>Get a <strong>FREE</strong></span><span>Assessment</span>
    <svg class="caret" viewBox="0 0 12 7"><polyline points="1,6 6,1 11,6" fill="none" stroke="#fff" stroke-width="2"/></svg></div>
</section>

<section class="banner strip" aria-label="Banner 468 by 60">
  <div class="brand">Learnwise<i></i></div>
  <div class="band center">
    <div class="y" style="font-size:18px;font-weight:800">1:1</div>
    <div class="y" style="font-size:13px">In-Home <strong class="w">Tutoring</strong></div>
    <div class="w" style="font-size:9px;margin-top:3px">The Best <span class="y">Tutor</span> For Your <span class="y">Child</span></div>
  </div>
  <div class="photo" role="img" aria-label="Tutor and schoolboy reading together by a bookshelf"></div>
  <svg class="notch" viewBox="0 0 12 36"><polygon points="0,0 12,18 0,36" fill="var(--blue)"/></svg>
  <div class="cta"><span class="big">FREE</span><span style="font-weight:400">Assessment</span><span>Find Out More</span>
    <svg class="caret" viewBox="0 0 12 7"><polyline points="1,6 6,1 11,6" fill="none" stroke="#fff" stroke-width="2"/></svg></div>
</section>

<section class="banner leader" aria-label="Leaderboard banner">
  <div class="brand">Learnwise<i></i></div>
  <div class="band center w">
    <div class="ratio">1:1</div>
    <div class="kind">In-Home<strong>Tutoring</strong></div>
    <div class="tag">The Best&nbsp; Tutor For Your Child</div>
  </div>
  <div class="photo" role="img" aria-label="Tutor working through a book with a schoolboy at a desk"></div>
  <svg class="notch" viewBox="0 0 16 90"><polygon points="0,0 4,0 16,45 4,90 0,90" fill="var(--yellow)"/><polygon points="0,0 12,45 0,90" fill="var(--orange)"/></svg>
  <div class="cta"><span class="big">FREE</span><span>Assessment</span><span>Find Out More</span>
    <svg class="caret" style="width:22px;height:11px" viewBox="0 0 12 7"><polyline points="1,6 6,1 11,6" fill="none" stroke="#fff" stroke-width="1.4"/></svg></div>
</section>

<section class="banner mobile" aria-label="Mobile leaderboard banner">
  <div class="brand">Learnwise<i></i></div>
  <div class="photo" role="img" aria-label="Tutor and schoolboy reading together at a desk"></div>
  <div class="cta"><span class="big">FREE</span><span style="font-weight:400">Assessment</span><span>Find Out More</span></div>
</section>

</body>
</html>
```